Marketing Brochure: Category Management – Assortment Optimization

Create a compelling a 1-page marketing brochure around a service that allows Brill International retailers to optimize their product assortments in their stores. The brochure must be fun, very professionally done, clean, and exciting to want possible clients to want to pick up. See word file for content details. The Brill Worldwide Partners red and white colors should be used. Also, include relevant photos to liven up the brochure.

Target Market(s)

Brill Toolworks Retailers in Different Parts of the World

Industry/Entity Type

Retail

Font styles to use
Sans Serif

Requirements
Must have
• See Word file. Add some really good photos relevant to retail.
• Red and White Colors would be good to match Brill Worldwide Partners logo
• Also, should look like a 'global' service. Maybe add a worldly look to it.
Nice to have
• See World file
Should not have
• N/A

```html
<!DOCTYPE html>
<html lang="en">
<head>
<meta charset="utf-8">
<title>Category Management – Assortment Optimization</title>
<link rel="stylesheet" href="https://fonts.googleapis.com/css2?family=Poppins:wght@300;400;600;700&family=Tinos&display=swap">
<style>
  :root {
    --brand-red: #e01b2c;
    --deep-red: #9b1111;
    --footer-red: #8e0e0c;
    --band-red: #8f0f0c;
    --bullet-grey: #8a8a8a;
    --body-ink: #2b2b2b;
    --paper: #ffffff;
    --backdrop: #e9eaea;
  }
  * { margin: 0; padding: 0; box-sizing: border-box; }
  html, body { width: 1200px; height: 900px; overflow: hidden; }
  body { background: var(--backdrop); position: relative; font-family: "Poppins", sans-serif; }

  .page { position: absolute; top: 60px; height: 756px; background: var(--paper); overflow: hidden; box-shadow: 0 10px 30px rgba(0,0,0,.12); }
  .page--front { left: 66px; width: 538px; }
  .page--back { left: 616px; width: 534px; }

  .abs { position: absolute; }

  /* front page */
  .photo { position: absolute; top: 0; height: 290px; }
  .photo--drywall { left: 0; width: 262px; background: linear-gradient(160deg, #b58a5c 0%, #8c6440 45%, #d9d3c9 70%, #6b4a2e 100%); }
  .photo--ladder { left: 276px; width: 262px; background: linear-gradient(200deg, #c49a68 0%, #9a7048 40%, #7a5a40 70%, #b88f63 100%); }
  .front-curve { position: absolute; left: 0; top: 240px; width: 538px; height: 80px; }
  .badge { position: absolute; border-radius: 50%; background: var(--paper); display: flex; align-items: center; justify-content: center; }
  .badge__dot { border-radius: 50%; background: var(--brand-red); }
  .badge--front { left: 203px; top: 202px; width: 132px; height: 132px; }
  .badge--front .badge__dot { width: 96px; height: 96px; }

  .title { position: absolute; left: 0; width: 538px; text-align: center; color: var(--deep-red); font-weight: 700; font-size: 32px; line-height: 42px; top: 347px; }
  .subtitle { position: absolute; left: 0; width: 538px; text-align: center; top: 440px; color: var(--brand-red); font-weight: 300; font-size: 14px; }
  .intro { position: absolute; left: 53px; width: 445px; top: 478px; font-family: "Tinos", serif; font-size: 10.6px; line-height: 12.8px; color: var(--body-ink); text-align: justify; text-align-last: center; }
  .intro p + p { margin-top: 12.8px; }

  .signature { position: absolute; left: 0; width: 538px; top: 694px; display: flex; justify-content: center; align-items: center; gap: 10px; }
  .signature__mark { width: 46px; height: 46px; border-radius: 50%; background: var(--brand-red); }
  .signature__name { font-weight: 600; font-size: 22px; color: var(--deep-red); }

  /* back page */
  .back-top { position: absolute; left: 0; top: 0; width: 534px; height: 120px; }
  .photo--arrows { position: absolute; right: 0; top: 60px; width: 240px; height: 170px; background: linear-gradient(140deg, #eef3f4 0%, #e4edf0 55%, #f2e5e4 100%); }
  .badge--back { left: 224px; top: 16px; width: 84px; height: 84px; }
  .badge--back .badge__dot { width: 60px; height: 60px; }

  .card { position: absolute; background: var(--paper); }
  .card--approach { left: 0; top: 118px; width: 476px; height: 200px; border-top-right-radius: 24px; }
  .photo--wood { position: absolute; left: 0; top: 318px; width: 534px; height: 302px; background: linear-gradient(170deg, #e6b98a 0%, #d79f6c 45%, #e8c199 100%); }
  .photo--roi { position: absolute; left: 0; top: 380px; width: 56px; height: 240px; background: linear-gradient(180deg, #e8474b 0%, #c81d26 60%, #e26a5d 100%); }
  .card--roi { left: 54px; top: 376px; width: 480px; height: 244px; border-top-left-radius: 24px; }

  .section-head { position: absolute; display: flex; align-items: center; gap: 10px; color: var(--brand-red); font-weight: 700; font-size: 19px; white-space: nowrap; }
  .section-head__rule { height: 2px; background: var(--brand-red); flex: 1; }
  .section-head--approach { left: 41px; top: 28px; width: 435px; }
  .section-head--roi { left: 43px; top: 24px; width: 437px; }

  .point { position: absolute; display: flex; align-items: center; gap: 7px; }
  .point__dot { flex: none; width: 20px; height: 20px; border-radius: 50%; background: var(--bullet-grey); }
  .point__text { font-weight: 700; font-size: 9.4px; line-height: 12.4px; color: var(--deep-red); letter-spacing: -0.1px; }

  .about { position: absolute; left: 0; top: 620px; width: 534px; height: 136px; background: var(--footer-red); color: var(--paper); }
  .about__head { position: absolute; top: 17px; width: 100%; text-align: center; font-weight: 700; font-size: 14px; }
  .about__body { position: absolute; left: 63px; width: 410px; top: 46px; font-family: "Tinos", serif; font-size: 10.6px; line-height: 12.8px; text-align: justify; text-align-last: center; }
</style>
</head>
<body>

<section class="page page--front">
  <div class="photo photo--drywall" role="img" aria-label="Worker lifting a drywall panel with a yellow panel hoist in a framed room"></div>
  <div class="photo photo--ladder" role="img" aria-label="Worker on an aluminium ladder installing ceiling fixtures among wooden framing"></div>
  <svg class="front-curve" viewBox="0 0 538 80" preserveAspectRatio="none" aria-hidden="true">
    <path d="M0 16 Q269 4 538 18 L538 80 L0 80 Z" fill="#ffffff"/>
  </svg>
  <div class="badge badge--front"><div class="badge__dot"></div></div>

  <h1 class="title">Category Management<br>Assortment Optimization</h1>
  <p class="subtitle">Satisfying Customers with Data-Driven, Informed Decisions</p>

  <div class="intro">
    <p>It takes a strong category strategy to drive sales growth. With changes in consumer demands and product introductions constantly making their way into the market, it’s not easy to optimize product selection toward maximizing market share and wider profit margins. To do so, companies need to quickly and effectively deploy well-established and nimble methodologies that refine and enhance category assortment and retail space decisions.</p>
    <p>Brill Worldwide Partners category management’s monthly services provides your business industry expertise, functional richness, and retail data analytics know-how to drive more profitable and productive product assortments. We speak analytics. In doing so, we synthesize raw data, assess it, and covert it into practical, measured solutions to help your business grow.</p>
  </div>

  <div class="signature">
    <div class="signature__mark"></div>
    <span class="signature__name">Brill Worldwide Partners</span>
  </div>
</section>

<section class="page page--back">
  <div class="photo--arrows" role="img" aria-label="Three-dimensional green, blue and red arrows pointing upward and outward"></div>
  <svg class="back-top" viewBox="0 0 534 120" preserveAspectRatio="none" aria-hidden="true">
    <path d="M0 0 H534 V28 Q300 70 0 52 Z" fill="#8f0f0c"/>
  </svg>
  <div class="badge badge--back"><div class="badge__dot"></div></div>

  <div class="card card--approach">
    <h2 class="section-head section-head--approach">Our Service Approach <span class="section-head__rule"></span></h2>
    <div class="point" style="left:43px;top:74px"><span class="point__dot"></span><span class="point__text">Understand your long-term vision,<br>market and assortment objectives</span></div>
    <div class="point" style="left:255px;top:74px"><span class="point__dot"></span><span class="point__text">Assess the current state of affairs to<br>your categories</span></div>
    <div class="point" style="left:43px;top:115px"><span class="point__dot"></span><span class="point__text">Obtain store level raw data one<br>category at a time</span></div>
    <div class="point" style="left:255px;top:115px"><span class="point__dot"></span><span class="point__text">Implement recommendations,<br>track results, and further advise</span></div>
    <div class="point" style="left:43px;top:157px"><span class="point__dot"></span><span class="point__text">Covert raw data into powerful insights about category<br>performance, opportunities, potential impact, and goal setting</span></div>
  </div>

  <div class="photo--wood" role="img" aria-label="Light wooden tabletop surface"></div>
  <div class="photo--roi" role="img" aria-label="Red letter cubes spelling ROI stacked on a table"></div>

  <div class="card card--roi">
    <h2 class="section-head section-head--roi">Return on Investment <span class="section-head__rule"></span></h2>
    <div class="point" style="left:43px;top:74px"><span class="point__dot"></span><span class="point__text">Increased profitability and<br>turnover</span></div>
    <div class="point" style="left:245px;top:74px"><span class="point__dot"></span><span class="point__text">Attack over-SKU’d categories<br>and less duplication</span></div>
    <div class="point" style="left:43px;top:115px"><span class="point__dot"></span><span class="point__text">Fact-based analytics with<br>collaborative market insights</span></div>
    <div class="point" style="left:245px;top:115px"><span class="point__dot"></span><span class="point__text">Acquired processes are<br>safeguarded for the long-term</span></div>
    <div class="point" style="left:43px;top:157px"><span class="point__dot"></span><span class="point__text">Reduce wasteful spending and<br>to help brands help retailers<br>compete more effectively</span></div>
    <div class="point" style="left:245px;top:157px"><span class="point__dot"></span><span class="point__text">Simplify assortments and planograms<br>create a more consumer-friendly<br>shopping experience</span></div>
    <div class="point" style="left:43px;top:205px"><span class="point__dot"></span><span class="point__text">The customer remains at the<br>heart of decision making</span></div>
  </div>

  <div class="about">
    <h3 class="about__head">About Brill Worldwide Partners</h3>
    <p class="about__body">Brill Worldwide Partners is a Brill International consulting service that provides training and strategy recommendations based on Brill’s 94-year retail industry expertise. Our services drive significant and sustainable performance improvements so you can accomplish your company’s most important business objectives</p>
  </div>
</section>

</body>
</html>
```